ZENITH conference Slide Deck

This is a conference for our team that will be 3 days of discussions on how to build our business in the middle of these challenging time. Its a bit of a battle and so we are going with a red and grey/black these although I am open to your interpretation. I will include a few graphics that we have started on to show you the look. But I am just getting started, INSPIRE ME! The screen will be 100' across the front of the room and these decks will show on each side and I will reformat for the middle 1X6 screen as needed. I have the AI file of the logo if you need it. I don't see where to upload it here.

Target Market(s)

our top producers

Industry/Entity Type

Real Estate Agent

Font styles to use
Sans Serif

Colors
ec1f27

Requirements
Must have
• Depth, creativity

```html
<!DOCTYPE html>
<html lang="en">
<head>
<meta charset="utf-8">
<title>ZENITH Conference – Slide Deck Overview</title>
<link rel="stylesheet" href="https://fonts.googleapis.com/css2?family=Archivo:wght@400;500;700;800&display=swap">
<style>
  :root{
    --red:#ec1f27;
    --wine:#3b0d10;
    --ink:#000;
    --coal:#111;
    --ash:#6b6b6b;
    --fog:#d9d9d9;
    --mist:#efefef;
    --paper:#fff;
  }
  *{margin:0;padding:0;box-sizing:border-box}
  html,body{width:1200px;height:675px;overflow:hidden;background:var(--paper)}
  body{position:relative;font-family:"Archivo",Arial,sans-serif;color:var(--ink)}
  .slide{position:absolute;overflow:hidden;background:var(--paper);box-shadow:0 4px 14px rgba(0,0,0,.12)}
  .abs{position:absolute}
  .wordmark{position:absolute;font-weight:700;color:var(--paper);letter-spacing:.04em;line-height:1;white-space:nowrap}
  .photo{position:absolute}
  .slide-title{position:absolute;left:12px;top:16px;font-size:9.5px;font-weight:400;white-space:nowrap}
  .slide-title b{font-weight:700}
  .footer{position:absolute;bottom:1px;right:6px;display:flex;align-items:center;gap:3px}
  .footer-num{width:9px;height:7px;background:var(--ink);color:#aaa;font-size:3px;display:flex;align-items:center;justify-content:center}
  .footer-name{font-size:4px;font-weight:700;color:var(--ink);letter-spacing:.04em}
  .tiny{font-size:3px;line-height:1.3}
  .small{font-size:3.6px;line-height:1.3}
  .white{color:var(--paper)}

  /* cover */
  .cover{left:77px;top:34px;width:523px;height:293px;background:var(--ink)}
  .cover .photo{inset:0;background:linear-gradient(100deg,#2a2a2a 0%,#4b4b4b 35%,#8a8a8a 60%,#5e5e5e 80%,#3a3a3a 100%)}
  .cover .band{left:0;top:0;width:131px;height:293px;background:linear-gradient(180deg,rgba(59,13,16,.94),rgba(40,8,10,.94))}
  .cover .shade{left:131px;top:0;right:0;bottom:0;background:linear-gradient(90deg,rgba(40,8,10,.55),rgba(0,0,0,0) 45%)}
  .cover h1{position:absolute;left:26px;top:118px;color:var(--paper);font-size:28px;line-height:1.05;font-weight:400;white-space:nowrap}
  .cover h1 b{font-weight:800;display:block}
  .cover .date{position:absolute;left:26px;top:184px;color:var(--paper);font-size:11px}

  /* thank you */
  .thanks{left:77px;top:352px;width:523px;height:293px;background:var(--ink)}
  .thanks .band{left:0;top:0;width:105px;height:293px;background:var(--coal)}
  .thanks h2{position:absolute;left:26px;top:30px;color:var(--paper);font-size:20px;font-weight:400}
  .thanks h2 b{font-weight:700}
  .thanks .copy{position:absolute;left:26px;top:61px;width:252px;color:var(--paper);font-size:6.3px;line-height:1.15}
  .thanks .copy p+p{margin-top:6px}
  .social{position:absolute;left:26px;top:218px;display:flex;gap:6px}
  .social span{width:14px;height:14px;border-radius:50%;background:#e6e6e6}

  /* section */
  .section{left:634px;top:34px;width:245px;height:137px;background:var(--ink)}
  .section .band{left:0;top:0;width:49px;height:137px;background:var(--coal)}
  .section .num{position:absolute;left:13px;top:50px;font-size:20px;font-weight:800;color:var(--paper)}
  .section .label{position:absolute;left:13px;top:73px;font-size:11px;font-weight:700;color:var(--paper)}
  .section .note{position:absolute;left:13px;top:87px;width:100px}

  /* table of content */
  .toc{left:912px;top:34px;width:245px;height:137px;background:transparent;box-shadow:none}
  .toc .sheet{left:0;top:0;width:245px;height:128px;background:var(--paper);box-shadow:0 4px 14px rgba(0,0,0,.12)}
  .toc .lead{position:absolute;left:12px;top:14px;font-size:9.5px}
  .toc .panel{left:113px;top:0;width:110px;height:121px;background:var(--ink)}
  .toc .edge{left:223px;top:0;width:22px;height:121px;background:var(--red)}
  .toc .gap{left:109px;top:0;width:4px;height:121px;background:var(--mist)}
  .toc-item{position:absolute;left:122px;display:flex;gap:5px;align-items:flex-start;color:var(--paper)}
  .toc-item .n{font-size:12px;font-weight:700;line-height:1}
  .toc-item .t{font-size:4.2px;font-weight:700;line-height:1.2}
  .toc-item .d{font-size:2.6px;font-weight:400;line-height:1.25;width:70px}
  .toc .footer{bottom:1px}

  .about{left:634px;top:190px;width:245px;height:137px}
  .perf{left:912px;top:190px;width:245px;height:137px}
  .process{left:634px;top:352px;width:245px;height:137px}
  .team{left:912px;top:352px;width:245px;height:137px}
  .custom-a{left:634px;top:508px;width:245px;height:137px}
  .custom-b{left:912px;top:508px;width:245px;height:137px}

  .card{position:absolute;top:30px;width:49px;height:90px;color:var(--paper)}
  .card .icon{position:absolute;left:6px;top:10px;width:37px;height:35px;display:flex;align-items:center;justify-content:center}
  .card .name{position:absolute;left:6px;top:52px;font-size:8px;font-weight:700}
  .card .txt{position:absolute;left:6px;top:63px;width:40px}

  .shot{position:absolute;top:30px;width:61px;height:90px;background:var(--mist)}
  .shot .cap{position:absolute;left:0;top:40px;width:61px;height:27px;padding:3px 4px;color:var(--paper)}
  .shot .cap b{font-size:5px;display:block;margin-bottom:1px}
  .meter{position:absolute;left:5px;width:50px;font-size:3px}
  .meter i{display:block;height:1.2px;background:#cfcfcf;margin-top:1px;position:relative}
  .meter i em{position:absolute;left:0;top:0;height:1.2px}
  .row{position:absolute;left:140px;width:93px;height:22.5px;color:var(--paper);display:flex;gap:4px;align-items:center;padding:0 4px}
  .row .n{font-size:8px;font-weight:700;flex:none}
  .row .body{display:flex;flex-direction:column;gap:1px}
  .row .head{font-size:5px;font-weight:700;line-height:1}

  .step{position:absolute;top:29px;height:39px;width:45px;background:var(--fog)}
  .step .n{position:absolute;left:4px;top:8px;font-size:10px;font-weight:700}
  .step .txt{position:absolute;left:4px;top:21px;width:37px}
  .block{position:absolute;top:68px;height:52px;padding:5px 4px;color:var(--paper);overflow:hidden}

  .member{position:absolute;top:29px;width:55px}
  .member .pic{height:68px}
  .member .tag{height:23px;color:var(--paper);text-align:center;padding-top:6px}
  .member .tag b{font-size:4.5px;display:block}
  .member .tag i{font-size:3px;display:block}
  .dots{display:flex;justify-content:center;gap:1.5px;margin-top:1.5px}
  .dots span{width:3.5px;height:3.5px;border-radius:50%;background:var(--paper)}

  .bar-track{position:absolute;height:1.4px;background:#cfcfcf}
  .bar-fill{position:absolute;height:1.4px;background:var(--ink)}

  .phase{position:absolute;top:29px;height:14px;color:var(--paper);font-size:4.5px;font-weight:600;display:flex;align-items:center;justify-content:center}
  .year{position:absolute;top:69px;width:32px}
  .year b{font-size:6px;display:block}
  .cell{position:absolute;top:95px;width:55px;height:25px;color:var(--paper);padding:3px 4px}
  .cell b{font-size:5px;display:block}
</style>
</head>
<body>

<section class="slide cover">
  <div class="photo" role="img" aria-label="Monochrome photo of a smiling woman holding a phone outdoors"></div>
  <div class="abs shade"></div>
  <div class="abs band"></div>
  <h1><b>Presentation</b>Template Guideline</h1>
  <div class="date">June 2020</div>
  <div class="wordmark" style="left:26px;top:256px;font-size:16px">ZENITH</div>
</section>

<section class="slide thanks">
  <div class="abs band"></div>
  <h2>Thank <b>You</b></h2>
  <div class="copy">
    <p>Lorem ipsum dolor sit amet, consectetur adipiscing elit. Sed a fermentum odio. Pellentesque vitae dictum ante. Aliquam erat volutpat. Maecenas neque diam, efficitur nec hendrerit at, dictum nec lectus. Proin lorem ante, vestibulum elementum fringilla nec, iaculis pharetra leo. Praesent ac varius dolor. Suspendisse sed facilisis lorem. Quisque tempor leo et mi ornare, eget semper arcu dignissim. Sed gravida molestie metus nec congue. Nunc blandit eros vulputate arcu luctus, ac mollis risus molestie.</p>
    <p>Mauris eu ipsum non orci tempus imperdiet a at elit. Proin mollis, enim et commodo feugiat, ante augue tincidunt arcu, blandit blandit nisi mauris ut massa. Praesent varius neque non ullamcorper luctus. Etiam consequat ultrices justo, quis hendrerit purus tempor quis. In non risus eu quam efficitur tristique eu non turpis. Proin sed varius lorem. Vivamus id lacus sollicitudin ante porta blandit.</p>
  </div>
  <div class="social" aria-label="Social channels"><span></span><span></span><span></span></div>
  <div class="wordmark" style="left:26px;top:262px;font-size:13px">ZENITH</div>
</section>

<section class="slide section">
  <div class="abs band"></div>
  <div class="num">01</div>
  <div class="label">Section Divider</div>
  <div class="note tiny white">Lorem ipsum dolor sit amet, consectetur adipiscing elit. Sed a fermentum odio. Pellentesque vitae dictum ante. Aliquam erat volutpat. Maecenas neque diam, efficitur nec hendrerit at, dictum nec lectus.</div>
  <div class="wordmark" style="left:13px;top:124px;font-size:6.5px">ZENITH</div>
</section>

<section class="slide toc">
  <div class="abs sheet"></div>
  <div class="lead">Table of Content</div>
  <div class="abs gap"></div>
  <div class="abs panel"></div>
  <div class="abs edge"></div>
  <div class="toc-item" style="top:22px"><span class="n">1</span><div><div class="t">Lorem ipsum dolor sit amet.</div><div class="d">Consectetur adipiscing elit. Sed a fermentum odio. Pellentesque vitae dictum ante.</div></div></div>
  <div class="toc-item" style="top:45px"><span class="n">2</span><div><div class="t">Lorem ipsum dolor sit amet.</div><div class="d">Consectetur adipiscing elit. Sed a fermentum odio. Pellentesque vitae dictum ante.</div></div></div>
  <div class="toc-item" style="top:69px"><span class="n">3</span><div><div class="t">Lorem ipsum dolor sit amet.</div><div class="d">Consectetur adipiscing elit. Sed a fermentum odio. Pellentesque vitae dictum ante.</div></div></div>
  <div class="toc-item" style="top:92px"><span class="n">4</span><div><div class="t">Lorem ipsum dolor sit amet.</div><div class="d">Consectetur adipiscing elit. Sed a fermentum odio. Pellentesque vitae dictum ante.</div></div></div>
  <div class="footer"><span class="footer-num">3</span><span class="footer-name">ZENITH</span></div>
</section>

<section class="slide about">
  <div class="slide-title">About the <b>Company</b></div>
  <div class="photo" style="left:160px;top:0;width:73px;height:120px;background:linear-gradient(160deg,#9a9a9a,#5a5a5a 55%,#2e2e2e)" role="img" aria-label="Monochrome photo of a team joining hands in celebration"></div>
  <div class="card" style="left:12px;background:var(--red)">
    <div class="icon" style="background:#f04a50"><svg width="14" height="14" viewBox="0 0 14 14"><circle cx="7" cy="7" r="5" fill="none" stroke="#fff" stroke-width="1.6"/><circle cx="7" cy="7" r="1.8" fill="#fff"/></svg></div>
    <div class="name">Target</div>
    <div class="txt small">Mauris eu ipsum non orci tempus imperdiet a at elit. Proin mollis, enim et commodo feugiat.</div>
  </div>
  <div class="card" style="left:61px;background:var(--ink)">
    <div class="icon" style="background:#2a2a2a"><svg width="12" height="14" viewBox="0 0 12 14"><path d="M6 1a4 4 0 0 0-2.4 7.2V10h4.8V8.2A4 4 0 0 0 6 1z" fill="#fff"/><rect x="3.8" y="11" width="4.4" height="1.3" fill="#fff"/></svg></div>
    <div class="name">Idea</div>
    <div class="txt small">Mauris eu ipsum non orci tempus imperdiet a at elit. Proin mollis, enim et commodo feugiat.</div>
  </div>
  <div class="card" style="left:110px;background:var(--ash)">
    <div class="icon" style="background:#7d7d7d"><svg width="12" height="14" viewBox="0 0 12 14"><rect x="1.5" y="2" width="9" height="11" fill="none" stroke="#fff" stroke-width="1.2"/><rect x="4" y="1" width="4" height="2" fill="#fff"/><path d="M3.5 6h5M3.5 8h5M3.5 10h5" stroke="#fff" stroke-width="1"/></svg></div>
    <div class="name">Survey</div>
    <div class="txt small">Mauris eu ipsum non orci tempus imperdiet a at elit. Proin mollis, enim et commodo feugiat.</div>
  </div>
  <div class="footer"><span class="footer-num">4</span><span class="footer-name">ZENITH</span></div>
</section>

<section class="slide perf">
  <div class="slide-title">Company Details <b>Performance</b></div>
  <div class="shot" style="left:12px">
    <div class="photo" style="left:0;top:0;width:61px;height:40px;background:linear-gradient(150deg,#b5b5b5,#6e6e6e)" role="img" aria-label="Photo of hands using a phone over a laptop"></div>
    <div class="cap" style="background:var(--red)"><b>High Payment</b><span class="tiny">Mauris eu ipsum non orci tempus imperdiet a at elit. Proin mollis.</span></div>
    <div class="meter" style="top:71px;color:var(--red)">Internal<i><em style="width:60%;background:var(--red)"></em></i></div>
    <div class="meter" style="top:80px">External<i><em style="width:75%;background:var(--ink)"></em></i></div>
  </div>
  <div class="shot" style="left:73px">
    <div class="photo" style="left:0;top:0;width:61px;height:40px;background:linear-gradient(150deg,#cfcfcf,#7c7c7c)" role="img" aria-label="Photo of a person shopping online on a tablet"></div>
    <div class="cap" style="background:var(--ink)"><b>Online Shop</b><span class="tiny">Mauris eu ipsum non orci tempus imperdiet a at elit. Proin mollis.</span></div>
    <div class="meter" style="top:71px;color:var(--red)">Internal<i><em style="width:85%;background:var(--red)"></em></i></div>
    <div class="meter" style="top:80px">External<i><em style="width:65%;background:var(--ink)"></em></i></div>
  </div>
  <div class="row" style="top:30px;background:var(--red)"><span class="n">01</span><div class="body"><span class="head">Requirements</span><span class="tiny">Mauris eu ipsum non orci tempus imperdiet a at elit. Proin mollis.</span></div></div>
  <div class="row" style="top:52.5px;background:var(--ink)"><span class="n">02</span><div class="body"><span class="head">Design</span><span class="tiny">Mauris eu ipsum non orci tempus imperdiet a at elit. Proin mollis.</span></div></div>
  <div class="row" style="top:75px;background:var(--red)"><span class="n">03</span><div class="body"><span class="head">Implementation</span><span class="tiny">Mauris eu ipsum non orci tempus imperdiet a at elit. Proin mollis.</span></div></div>
  <div class="row" style="top:97.5px;background:var(--ink)"><span class="n">04</span><div class="body"><span class="head">Deployment</span><span class="tiny">Mauris eu ipsum non orci tempus imperdiet a at elit. Proin mollis.</span></div></div>
  <div class="footer"><span class="footer-num">5</span><span class="footer-name">ZENITH</span></div>
</section>

<section class="slide process">
  <div class="slide-title">Process <b>Infographic</b></div>
  <div class="step" style="left:12px"><span class="n">01</span><div class="txt tiny">Etiam consequat ultrices justo, quis hendrerit puru tempor.</div></div>
  <div class="step" style="left:56px"><span class="n">02</span><div class="txt tiny">Etiam consequat ultrices justo, quis hendrerit puru tempor.</div></div>
  <div class="step" style="left:100px"><span class="n">03</span><div class="txt tiny">Etiam consequat ultrices justo, quis hendrerit puru tempor.</div></div>
  <div class="step" style="left:144px"><span class="n">04</span><div class="txt tiny">Etiam consequat ultrices justo, quis hendrerit puru tempor.</div></div>
  <div class="step" style="left:188px"><span class="n">05</span><div class="txt tiny">Etiam consequat ultrices justo, quis hendrerit puru tempor.</div></div>
  <svg class="abs" style="left:12px;top:29px" width="221" height="39" viewBox="0 0 221 39" aria-hidden="true">
    <g fill="none" stroke="#fff" stroke-width="1.4"><path d="M42 0l6 6-6 6"/><path d="M86 0l6 6-6 6"/><path d="M130 0l6 6-6 6"/><path d="M174 0l6 6-6 6"/></g>
  </svg>
  <div class="block tiny" style="left:12px;width:88px;background:var(--red)">Lorem ipsum dolor sit amet, consectetur adipiscing elit. Sed a fermentum odio. Pellentesque vitae dictum ante. Aliquam erat volutpat. Maecenas neque diam, efficitur nec hendrerit at, dictum nec lectus. Proin lorem ante, vestibulum elementum fringilla nec, iaculis pharetra leo. Praesent ac varius dolor.</div>
  <div class="block tiny" style="left:100px;width:88px;background:var(--ink)">Lorem ipsum dolor sit amet, consectetur adipiscing elit. Sed a fermentum odio. Pellentesque vitae dictum ante. Aliquam erat volutpat. Maecenas neque diam, efficitur nec hendrerit at, dictum nec lectus. Proin lorem ante, vestibulum elementum fringilla nec, iaculis pharetra leo. Praesent ac varius dolor.</div>
  <div class="block tiny" style="left:188px;width:45px;background:var(--ash)">Lorem ipsum dolor sit amet, consectetur adipiscing elit. Sed a fermentum odio. Pellentesque vitae dictum ante. Aliquam erat volutpat.</div>
  <div class="footer"><span class="footer-num">6</span><span class="footer-name">ZENITH</span></div>
</section>

<section class="slide team">
  <div class="slide-title">Our <b>Team</b></div>
  <div class="member" style="left:12px"><div class="pic" style="background:linear-gradient(180deg,#5a5a5a,#2c2c2c)" role="img" aria-label="Portrait photo of a team member"></div><div class="tag" style="background:var(--red)"><b>Your Name</b><i>Job Position</i><div class="dots"><span></span><span></span><span></span></div></div></div>
  <div class="member" style="left:67px"><div class="pic" style="background:linear-gradient(180deg,#d8d8d8,#8e8e8e)" role="img" aria-label="Portrait photo of a team member"></div><div class="tag" style="background:var(--ink)"><b>Your Name</b><i>Job Position</i><div class="dots"><span></span><span></span><span></span></div></div></div>
  <div class="member" style="left:122px"><div class="pic" style="background:linear-gradient(180deg,#7a7a7a,#3e3e3e)" role="img" aria-label="Portrait photo of a team member"></div><div class="tag" style="background:var(--red)"><b>Your Name</b><i>Job Position</i><div class="dots"><span></span><span></span><span></span></div></div></div>
  <div class="member" style="left:178px"><div class="pic" style="background:linear-gradient(180deg,#e2e2e2,#9a9a9a)" role="img" aria-label="Portrait photo of a team member"></div><div class="tag" style="background:var(--ink)"><b>Your Name</b><i>Job Position</i><div class="dots"><span></span><span></span><span></span></div></div></div>
  <div class="footer"><span class="footer-num">7</span><span class="footer-name">ZENITH</span></div>
</section>

<section class="slide custom-a">
  <div class="slide-title">Custom <b>Infographic</b></div>
  <div class="block tiny" style="left:12px;top:29px;width:43px;height:46px;background:var(--red)">Praesent varius neque non ullamcorper luctus. Etiam consequat ultrices justo, quis hendrerit purus tempor quis.</div>
  <div class="block tiny" style="left:12px;top:75px;width:43px;height:45px;background:var(--ink)">Mauris eu ipsum non orci tempus imperdiet a at elit. Proin mollis, enim et commodo feugiat, ante augue tincidunt arcu.</div>
  <div class="abs" style="left:55px;top:29px;width:178px;height:91px;background:var(--mist)"></div>
  <div class="photo" style="left:160px;top:40px;width:65px;height:80px;background:linear-gradient(160deg,#dcdcdc,#8a8a8a 60%,#4a4a4a)" role="img" aria-label="Photo of a hand holding a smartphone showing a house"></div>
  <div class="abs" style="left:71px;top:50px;font-size:11px;font-weight:700;color:var(--red)">1</div>
  <div class="abs" style="left:80px;top:51px;font-size:4.5px;font-weight:700;color:var(--red)">Lorem ipsum.</div>
  <div class="abs tiny" style="left:80px;top:57px;width:40px">Pellentesque mollis vel lectus eget posuere. Praesent vitae nibh rutrum.</div>
  <div class="bar-track" style="left:80px;top:71px;width:44px"></div><div class="bar-fill" style="left:80px;top:71px;width:26px"></div>
  <div class="abs" style="left:127px;top:69.5px;font-size:3.5px;font-weight:700;color:var(--red)">60%</div>
  <div class="abs" style="left:71px;top:84px;font-size:11px;font-weight:700">2</div>
  <div class="abs" style="left:80px;top:85px;font-size:4.5px;font-weight:700">Lorem ipsum.</div>
  <div class="abs tiny" style="left:80px;top:91px;width:40px">Pellentesque mollis vel lectus eget posuere. Praesent vitae nibh rutrum.</div>
  <div class="bar-track" style="left:80px;top:105px;width:44px"></div><div class="bar-fill" style="left:80px;top:105px;width:35px"></div>
  <div class="abs" style="left:127px;top:103.5px;font-size:3.5px;font-weight:700">80%</div>
  <svg class="abs" style="left:110px;top:45px" width="60" height="60" viewBox="0 0 60 60" aria-hidden="true">
    <path d="M12 5h38" stroke="#ec1f27" stroke-width=".5" fill="none"/><path d="M12 39h38" stroke="#555" stroke-width=".5" fill="none"/>
  </svg>
  <div class="footer"><span class="footer-num">8</span><span class="footer-name">ZENITH</span></div>
</section>

<section class="slide custom-b">
  <div class="slide-title">Custom <b>Infographic</b></div>
  <div class="phase" style="left:12px;width:83px;background:var(--red)">Requirements</div>
  <div class="phase" style="left:95px;width:34px;background:var(--ink)">Design</div>
  <div class="phase" style="left:129px;width:49px;background:var(--red)">Implementation</div>
  <svg class="abs" style="left:178px;top:29px" width="59" height="14" viewBox="0 0 59 14" aria-hidden="true"><path d="M0 0h52l5 7-5 7H0z" fill="#000"/></svg>
  <div class="phase" style="left:178px;width:52px;background:transparent">Deployment</div>
  <div class="abs" style="left:12px;top:55px;width:219px;height:1.6px;background:#d4d4d4"></div>
  <div class="abs" style="left:12px;top:55px;width:83px;height:1.6px;background:var(--red)"></div>
  <svg class="abs" style="left:10px;top:52px" width="225" height="16" viewBox="0 0 225 16" aria-hidden="true">
    <circle cx="2.5" cy="3.8" r="2" fill="#ec1f27"/>
    <g stroke="#ec1f27" stroke-width=".7"><path d="M4 4v9M42 4v9M80 4v9"/></g>
    <path d="M221 1l3 3-3 3" fill="none" stroke="#d4d4d4" stroke-width=".8"/>
  </svg>
  <div class="year" style="left:12px;color:var(--red)"><b>2018</b><span class="tiny" style="color:#000">Mauris eu ipsum non orci tempus a at elit.</span></div>
  <div class="year" style="left:50px;color:var(--red)"><b>2019</b><span class="tiny" style="color:#000">Mauris eu ipsum non orci tempus a at elit.</span></div>
  <div class="year" style="left:88px;color:var(--red)"><b>2020</b><span class="tiny" style="color:#000">Mauris eu ipsum non orci tempus a at elit.</span></div>
  <div class="year" style="left:126px;color:#777"><b>2021</b><span class="tiny">Mauris eu ipsum non orci tempus a at elit.</span></div>
  <div class="year" style="left:164px;color:#777"><b>2022</b><span class="tiny">Mauris eu ipsum non orci tempus a at elit.</span></div>
  <div class="year" style="left:202px;color:#777"><b>2023</b><span class="tiny">Mauris eu ipsum non orci tempus a at elit.</span></div>
  <div class="cell" style="left:12px;background:var(--red)"><b>Fast</b><span class="tiny">Mauris eu ipsum non orci tempus imperdiet a at elit.</span></div>
  <div class="cell" style="left:67px;background:var(--ink)"><b>Contact</b><span class="tiny">Mauris eu ipsum non orci tempus imperdiet a at elit.</span></div>
  <div class="cell" style="left:122px;background:var(--red)"><b>Performance</b><span class="tiny">Mauris eu ipsum non orci tempus imperdiet a at elit.</span></div>
  <div class="cell" style="left:178px;background:var(--ink)"><b>Document</b><span class="tiny">Mauris eu ipsum non orci tempus imperdiet a at elit.</span></div>
  <div class="footer"><span class="footer-num">9</span><span class="footer-name">ZENITH</span></div>
</section>

</body>
</html>
```